Copperleaf Motorized Shade Business Card

Hello, we've had our logo made. Now we are looking for a clean and cool looking business card. One side can just be the logo with any design elements that might look good with it. The other side will be Name, Phone Number and Email. There will not be an address on the card.

```html
<!DOCTYPE html>
<html lang="en">
<head>
<meta charset="utf-8">
<title>Copperleaf Motorized Shade Business Card</title>
<link rel="stylesheet" href="https://fonts.googleapis.com/css2?family=Montserrat:wght@300;400;600;700&display=swap">
<style>
  :root {
    --backdrop: #d3e2dc;
    --navy: #1a2440;
    --brand-navy: #1c3b78;
    --royal: #0a5cb0;
    --cyan: #04c0ef;
    --sun: #fdb913;
    --paper: #ffffff;
  }
  * { box-sizing: border-box; margin: 0; padding: 0; }
  html, body {
    width: 1200px; height: 856px; overflow: hidden;
    background: var(--backdrop);
    font-family: "Montserrat", sans-serif;
  }
  .canvas { position: relative; width: 1200px; height: 856px; }
  .card {
    position: absolute; width: 640px; height: 366px;
    border-radius: 28px; overflow: hidden;
    box-shadow: 0 14px 30px rgba(30, 50, 60, 0.18);
  }
  .card svg { position: absolute; inset: 0; width: 100%; height: 100%; }
  .card--back { left: 500px; top: 56px; }
  .card--front { left: 60px; top: 440px; }

  .brand {
    position: absolute; display: flex; align-items: center; gap: 10px;
    color: var(--brand-navy); font-weight: 700; white-space: nowrap;
  }
  .brand__dot { border-radius: 50%; background: var(--sun); flex: none; }
  .card--front .brand { left: 0; right: 0; top: 104px; justify-content: center; font-size: 27px; }
  .card--front .brand__dot { width: 26px; height: 26px; }
  .card--back .brand { right: 30px; top: 44px; font-size: 15px; }
  .card--back .brand__dot { width: 14px; height: 14px; }

  .holder { position: absolute; left: 40px; top: 44px; color: var(--paper); }
  .holder__name { font-size: 25px; letter-spacing: 0.5px; font-weight: 300; }
  .holder__name b { font-weight: 700; }
  .holder__role { font-size: 14px; font-weight: 300; margin-top: 2px; letter-spacing: 0.5px; }
  .holder__rule { width: 56px; height: 3px; background: var(--cyan); margin-top: 8px; }

  .contacts { position: absolute; left: 40px; bottom: 40px; color: var(--paper); }
  .contact { display: flex; align-items: center; gap: 14px; margin-top: 12px; }
  .contact__icon {
    width: 34px; height: 34px; border-radius: 50%; background: var(--cyan);
    display: flex; align-items: center; justify-content: center; flex: none;
  }
  .contact__icon svg { width: 18px; height: 18px; position: static; }
  .contact__lines { font-size: 13px; line-height: 1.35; font-weight: 400; }
</style>
</head>
<body>
<main class="canvas">

  <section class="card card--back" aria-label="Card back with contact details">
    <svg viewBox="0 0 640 366" preserveAspectRatio="none" aria-hidden="true">
      <rect width="640" height="366" fill="var(--navy)"/>
      <path d="M240 0 C280 130 390 240 640 305 L640 0 Z" fill="var(--sun)"/>
      <path d="M262 0 C300 140 420 245 640 292 L640 0 Z" fill="var(--royal)"/>
      <path d="M282 0 C320 120 440 215 640 272 L640 0 Z" fill="var(--cyan)"/>
      <path d="M300 0 C340 110 470 178 640 188 L640 0 Z" fill="var(--paper)"/>
    </svg>
    <div class="brand"><span class="brand__dot"></span>Copperleaf Motorized Shade</div>
    <div class="holder">
      <p class="holder__name"><b>DANA</b> WHITFIELD</p>
      <p class="holder__role">CEO DIRECTOR</p>
      <div class="holder__rule"></div>
    </div>
    <div class="contacts">
      <div class="contact">
        <span class="contact__icon">
          <svg viewBox="0 0 24 24"><rect x="7" y="2" width="10" height="20" rx="2" fill="none" stroke="#fff" stroke-width="2"/><circle cx="12" cy="18" r="1.2" fill="#fff"/></svg>
        </span>
        <p class="contact__lines">+000 12345 6789<br>+000 12345 6789</p>
      </div>
      <div class="contact">
        <span class="contact__icon">
          <svg viewBox="0 0 24 24"><rect x="3" y="6" width="18" height="12" rx="1" fill="#fff"/><path d="M3 6 L12 13 L21 6" fill="none" stroke="var(--cyan)" stroke-width="1.6"/></svg>
        </span>
        <p class="contact__lines">dana@copperleafshade.com<br>copperleafshade.com</p>
      </div>
    </div>
  </section>

  <section class="card card--front" aria-label="Card front with brand name">
    <svg viewBox="0 0 640 366" preserveAspectRatio="none" aria-hidden="true">
      <rect width="640" height="366" fill="var(--paper)"/>
      <path d="M230 366 Q470 250 640 62 L640 366 Z" fill="var(--cyan)"/>
      <path d="M200 366 Q470 268 640 148 L640 366 Z" fill="var(--royal)"/>
      <path d="M0 282 Q220 262 420 205 Q230 282 0 322 Z" fill="var(--sun)"/>
      <path d="M0 318 Q300 252 640 178 L640 366 L0 366 Z" fill="var(--navy)"/>
    </svg>
    <div class="brand"><span class="brand__dot"></span>Copperleaf Motorized Shade</div>
  </section>

</main>
</body>
</html>
```